" Quintela advogados é um escritório de advocacia de grande porte atuando em 6 Estados, sendo em 3 deles temos filial em funcionamento, além da matriz (Curitiba). "

```html
<!DOCTYPE html>
<html lang="pt-BR">
<head>
<meta charset="utf-8">
<title>Quintela Advogados — Envelope</title>
<link rel="stylesheet" href="https://fonts.googleapis.com/css2?family=Cinzel:wght@400;500&family=Montserrat:wght@400;500&display=swap">
<style>
  :root {
    --bg: #e9e6e1;
    --paper: #ffffff;
    --paper-shade: #f2f2f2;
    --navy-top: #26313c;
    --navy-bottom: #0d131a;
    --gold: #c9a15a;
    --ink: #1e1e1e;
    --ghost: #e3e3e3;
    --white: #f5f5f5;
  }
  * { margin: 0; padding: 0; box-sizing: border-box; }
  html, body { width: 1200px; height: 1200px; overflow: hidden; background: var(--bg); }
  .canvas { position: relative; width: 1200px; height: 1200px; }
  .envelope-art { position: absolute; inset: 0; }

  .back-watermark {
    position: absolute; left: 120px; top: 520px; width: 445px;
    text-align: center;
    font-family: "Cinzel", serif; font-weight: 400; font-size: 78px;
    letter-spacing: 4px; color: var(--ghost);
  }

  .contact-block {
    position: absolute; left: 330px; top: 826px; width: 220px;
    font-family: "Montserrat", sans-serif; font-size: 9.5px; line-height: 15px;
    color: var(--ink); text-align: right;
  }
  .contact-line { display: flex; justify-content: flex-end; align-items: center; gap: 6px; }
  .contact-line svg { width: 9px; height: 9px; flex: none; }

  .front-identity {
    position: absolute; left: 575px; top: 505px; width: 495px;
    display: flex; flex-direction: column; align-items: center;
    color: var(--white); font-family: "Cinzel", serif; font-weight: 400;
  }
  .identity-square { width: 52px; height: 52px; background: var(--gold); margin-bottom: 34px; }
  .identity-name { font-size: 46px; letter-spacing: 5px; line-height: 1; }
  .identity-tag { font-size: 15px; letter-spacing: 9px; margin-top: 14px; padding-left: 9px; }
</style>
</head>
<body>
<main class="canvas">
  <svg class="envelope-art" width="1200" height="1200" viewBox="0 0 1200 1200" aria-hidden="true">
    <defs>
      <linearGradient id="navy-fill" x1="0" y1="0" x2="1" y2="1">
        <stop offset="0" stop-color="var(--navy-top)"/>
        <stop offset="0.55" stop-color="#141c24"/>
        <stop offset="1" stop-color="var(--navy-bottom)"/>
      </linearGradient>
    </defs>
    <!-- back of envelope, white -->
    <path class="envelope-back" fill="var(--paper)"
      d="M120 290 L152 290 L160 312 L530 312 L538 290 L565 290 L565 1130 L120 1130 Z"/>
    <path fill="var(--paper-shade)" d="M565 960 L575 960 L575 1130 L565 1130 Z"/>
    <!-- front of envelope, navy -->
    <path class="envelope-front" fill="url(#navy-fill)"
      d="M590 283 L1035 283 Q1050 283 1052 298 L1055 340 L1066 350 Q1070 354 1070 362 L1070 1118 Q1070 1130 1058 1130 L587 1130 Q575 1130 575 1118 L575 298 Q575 283 590 283 Z"/>
  </svg>

  <div class="back-watermark">QUINTELA</div>

  <address class="contact-block">
    <div class="contact-line">+55 41 3210-4455
      <svg viewBox="0 0 10 10"><path d="M2 1 L4 1 L4.5 3 L3.4 4 Q4.5 6 6 6.6 L7 5.5 L9 6 L9 8 Q8.5 9 7.5 9 Q1 8 1 2.5 Q1 1 2 1 Z" fill="var(--ink)"/></svg></div>
    <div class="contact-line">+55 41 9876-2201
      <svg viewBox="0 0 10 10"><rect x="2.5" y="0.5" width="5" height="9" rx="1" fill="none" stroke="var(--ink)"/><circle cx="5" cy="8" r="0.6" fill="var(--ink)"/></svg></div>
    <div class="contact-line">R. das Araucárias, 120, PR
      <svg viewBox="0 0 10 10"><path d="M5 9.5 L2 5 A3.3 3.3 0 1 1 8 5 Z" fill="var(--ink)"/><circle cx="5" cy="3.6" r="1.2" fill="var(--paper)"/></svg></div>
    <div class="contact-line">contato@quintela.adv.br
      <svg viewBox="0 0 10 10"><rect x="0.5" y="2" width="9" height="6" fill="var(--ink)"/><path d="M0.5 2 L5 5.5 L9.5 2" fill="none" stroke="var(--paper)" stroke-width="0.8"/></svg></div>
    <div class="contact-line">www.quintela.adv.br
      <svg viewBox="0 0 10 10"><circle cx="5" cy="5" r="4.3" fill="none" stroke="var(--ink)"/><path d="M0.7 5 H9.3 M5 0.7 Q2.5 5 5 9.3 M5 0.7 Q7.5 5 5 9.3" fill="none" stroke="var(--ink)" stroke-width="0.7"/></svg></div>
  </address>

  <section class="front-identity">
    <div class="identity-square"></div>
    <div class="identity-name">QUINTELA</div>
    <div class="identity-tag">ADVOGADOS</div>
  </section>
</main>
</body>
</html>
```